Calloway Teaching Placements Business Cards

We need business cards designed for our growing recruitment business.
We have just launched our offices in Sydney Melbourne and have a well established business in Perth. We are a fun young firm that specialise in Early Years Education Recruitment.
Our vision mission values are below
Our Vision:
To be:
the single, nationally recognised leader in the Early Childhood Sector.
a multifaceted organisation with a network of expertly driven facilities in the Early Childhood Sector, acknowledged as an organisation of integrity, innovation, heart and community.

Our Mission:
To provide superior quality recruitment services and solutions to the Early Childhood sector.
We empower our candidates to succeed.
We engage in trusted partnerships with our clients.
We grow our business/network/community, with passion and integrity.

Our Values:

We… are REAL
think: CUSTOMER
find: SOLUTIONS
achieve: RESULTS
enjoy: WHAT WE DO

Our website is www.callowayteaching.com feel free to visit it for inspiration.
Name Felix Harrowby
Title National Director
1300 047 815
0412 736 205
felix@callowayplacements.com
website www.callowayteaching.com

I have attached our current business cards and logo designs to view

Target Market(s)

Recruitment

Industry/Entity Type

Business

Contact Information for Business Card

Name Felix Harrowby
Title National Director
1300 047 815
0412 736 205

Font styles to use
Serif

Requirements
Must have
• Company Values and the cities we have offices in Perth | Sydney | Melbourne
Nice to have
• Our Vision on the card
• Our Vision:
• To be a nationally recognised leader in the Early Childhood Sector.
• A multifaceted organisation with a network of expertly driven facilities in the Early Childhood Sector, acknowledged as an organisation of integrity, innovation, heart and community.

```html
<!DOCTYPE html>
<html lang="en">
<head>
<meta charset="utf-8">
<title>Calloway Teaching Placements – Business Cards</title>
<link rel="stylesheet" href="https://fonts.googleapis.com/css2?family=Lora:wght@400;500;600&display=swap">
<style>
  :root {
    --backdrop: #8a8c8e;
    --card-white: #ecedef;
    --navy: #1b3f66;
    --navy-deep: #0d3457;
    --blue-bright: #2497cf;
    --blue-mid: #1d6ea8;
    --grey-text: #555a60;
    --rule: #8f9398;
    --ring: #e6edf3;
    --values-text: #dbe8f2;
  }
  * { margin: 0; padding: 0; box-sizing: border-box; }
  html, body {
    width: 1105px; height: 1200px; overflow: hidden;
    background: var(--backdrop);
    font-family: "Lora", Georgia, serif;
  }
  .canvas { position: relative; width: 1105px; height: 1200px; }

  .card { position: absolute; left: 182px; width: 747px; overflow: hidden; }

  /* Front */
  .card-front { top: 119px; height: 426px; background: var(--card-white); }
  .card-front .base-band {
    position: absolute; left: 0; right: 0; bottom: 0; height: 14px;
    background: linear-gradient(90deg, var(--navy-deep), var(--blue-bright) 50%, var(--navy-deep));
    border-top: 2px solid #c9cdd1;
  }
  .brand { position: absolute; left: 364px; top: 33px; display: flex; align-items: center; gap: 10px; }
  .brand-mark { width: 102px; height: 102px; flex: none; }
  .brand-name { font-size: 21px; font-weight: 500; color: var(--navy); letter-spacing: 0.4px; line-height: 1.1; white-space: nowrap; }
  .brand-tagline { font-size: 11.5px; font-weight: 600; color: var(--blue-mid); margin-top: 6px; white-space: nowrap; }

  .person { position: absolute; left: 41px; top: 186px; }
  .person-name { font-size: 29px; font-weight: 600; color: var(--navy); letter-spacing: 0.3px; line-height: 1.2; }
  .person-title { font-size: 20px; font-weight: 500; color: var(--grey-text); margin-top: 1px; }

  .divider { position: absolute; left: 41px; width: 662px; top: 264px; height: 2px; background: var(--rule); }

  .contacts { position: absolute; left: 41px; top: 278px; list-style: none; }
  .contacts li { display: flex; align-items: center; gap: 8px; height: 27.7px; font-size: 19px; color: var(--grey-text); white-space: nowrap; }
  .contacts svg { width: 18px; height: 18px; flex: none; fill: var(--navy); }

  .offices { position: absolute; right: 40px; top: 308px; list-style: none; text-align: right; }
  .offices li { display: flex; justify-content: flex-end; align-items: center; gap: 10px; height: 26px; font-size: 19px; color: var(--grey-text); }
  .offices li::after { content: ""; width: 7px; height: 7px; border-radius: 50%; background: var(--navy); }

  /* Back */
  .card-back {
    top: 635px; height: 428px;
    background: radial-gradient(ellipse 65% 75% at 50% 50%, var(--blue-bright) 0%, var(--blue-mid) 45%, var(--navy-deep) 100%);
  }
  .values { position: absolute; left: 44px; top: 44px; color: var(--values-text); }
  .values-heading { font-size: 15px; font-weight: 600; letter-spacing: 1.5px; text-transform: uppercase; color: var(--ring); margin-bottom: 10px; }
  .values-list { list-style: none; }
  .values-list li { font-size: 17px; font-weight: 400; line-height: 29px; }
  .values-list strong { font-weight: 600; color: var(--ring); letter-spacing: 0.5px; }

  .back-brand { position: absolute; right: 34px; bottom: 34px; display: flex; align-items: center; gap: 14px; }
  .back-brand-name { font-size: 16px; font-weight: 500; color: var(--ring); letter-spacing: 0.5px; white-space: nowrap; }
  .back-brand-ring { width: 146px; height: 146px; border: 4px solid var(--ring); border-radius: 50%; }
</style>
</head>
<body>
<main class="canvas">

  <section class="card card-front" aria-label="Business card front">
    <div class="brand">
      <svg class="brand-mark" viewBox="0 0 102 102" aria-hidden="true">
        <circle cx="51" cy="51" r="48" fill="none" stroke="#1d6ea8" stroke-width="3"/>
      </svg>
      <div>
        <p class="brand-name">CALLOWAY TEACHING</p>
        <p class="brand-tagline">Bringing quality to education recruitment</p>
      </div>
    </div>

    <div class="person">
      <h1 class="person-name">Felix Harrowby</h1>
      <p class="person-title">National Director</p>
    </div>

    <div class="divider"></div>

    <ul class="contacts">
      <li>
        <svg viewBox="0 0 24 24"><path d="M6.6 10.8a15.1 15.1 0 0 0 6.6 6.6l2.2-2.2c.3-.3.7-.4 1-.2 1.1.4 2.3.6 3.6.6.6 0 1 .4 1 1V20c0 .6-.4 1-1 1A17 17 0 0 1 3 4c0-.6.4-1 1-1h3.5c.6 0 1 .4 1 1 0 1.3.2 2.5.6 3.6.1.3 0 .7-.2 1z"/></svg>
        1300 047 815
      </li>
      <li>
        <svg viewBox="0 0 24 24"><path d="M6 3h12v5H6zM4 9h16a2 2 0 0 1 2 2v6h-4v4H6v-4H2v-6a2 2 0 0 1 2-2zm4 7v3h8v-3z"/></svg>
        0412 736 205
      </li>
      <li>
        <svg viewBox="0 0 24 24"><path d="M2 5h20v14H2zm2 2v.5l8 5 8-5V7z"/></svg>
        felix@callowayplacements.com
      </li>
      <li>
        <svg viewBox="0 0 24 24"><circle cx="12" cy="12" r="10"/><path d="M8 6c2 1 1 3 3 3s1 3-1 4-1 4-3 3M15 15c1-2 4-2 4 0" fill="none" stroke="#ecedef" stroke-width="1.6"/></svg>
        www.callowayteaching.com
      </li>
    </ul>

    <ul class="offices">
      <li>Perth</li>
      <li>Sydney</li>
      <li>Melbourne</li>
    </ul>

    <div class="base-band"></div>
  </section>

  <section class="card card-back" aria-label="Business card back">
    <div class="values">
      <p class="values-heading">Our Values</p>
      <ul class="values-list">
        <li>We… are <strong>REAL</strong></li>
        <li>think: <strong>CUSTOMER</strong></li>
        <li>find: <strong>SOLUTIONS</strong></li>
        <li>achieve: <strong>RESULTS</strong></li>
        <li>enjoy: <strong>WHAT WE DO</strong></li>
      </ul>
    </div>
    <div class="back-brand">
      <span class="back-brand-name">CALLOWAY TEACHING</span>
      <div class="back-brand-ring"></div>
    </div>
  </section>

</main>
</body>
</html>
```